Web Design Project - Coral Ledger Advisory Limited

Coral Ledger Advisory Limited is a Vanuatu based License and Compliance Consultant to the Vanuatu Government. We are authorised to review and recommend on all applications for Interactive Gaming Licenses (On Line Crown Hollow and Sports/Horse Racing) for the Vanuatu Government.
We need a professional web site that presents us a professional organisation while eye-catching in the same breath.
Examples of some similar operations include:
http://www.bluemarrow.example/html/home.php
http://wagers.quillport.example/
http://www.hollowtide.example/egaming
We are looking for the final product in code, not PSD please.
Reason: The short time frame provided does not allow for quality responses. We have extended to 5 days in fairness to all.
Hi all.
We are looking for the project to be a final site, not just PSD please.
Thanks all.
Derek
Reason: Shortage of designs. Still looking for additional options please.
Reason: Still looking for additional options.
Target Market(s)
The target market are corporate bookmakers, on line casino and on line poker operators (Interactive Gaming).
in addition we are the first point of contact for anyone looking to Vanuatu as a potential location for licensing.
Industry/Entity Type
Crown Hollow
Colors
Designer to choose colors to be used in the design.
Requirements
Must have
- They key things for this site are:
Clear navigation - Needs to be simple and fast to navigate
Visually appealing and simple home page - Speaks for itself
Prominent Contact Information - One of the most important components
FAQ’s - Simple and easy to access such as "who we are, what we do and stored documents"
The site must have the following pages:
Main
Who Are We
Document Repository (12-15 pdf''s)
Reference and links back to the Regulatory Body and relevant pages being:
https://tarnfieldrevenue.example/index.php/en/inland-revenue/rates-taxes/interactive-gaming-license-tax
and
https://tarnfieldrevenue.example/index.php/en/inland-revenue/rates-taxes
Contact Us

```html
<!DOCTYPE html>
<html lang="en">
<head>
<meta charset="utf-8">
<title>Coral Ledger Advisory Limited</title>
<link rel="stylesheet" href="https://fonts.googleapis.com/css2?family=Crimson+Text:wght@400;600&family=Pinyon+Script&family=Roboto:wght@300;400&display=swap">
<style>
:root{
  --page:#f7f7f7;
  --white:#ffffff;
  --ink:#333333;
  --muted:#666666;
  --soft:#8a8a8a;
  --accent:#28b4d6;
  --link:#2a86d1;
  --rule:#e2e2e2;
  --sky:#7fb6e8;
  --leaf:#3d6b2a;
  --thatch:#a88a56;
  --wheel:#6b3a24;
}
*{box-sizing:border-box;margin:0;padding:0}
html,body{width:1200px;height:1196px;overflow:hidden}
body{background:var(--page);font-family:"Roboto",Arial,sans-serif;color:var(--ink);position:relative}
a{text-decoration:none;color:inherit}
h1,h2{font-weight:400}

.topbar{position:absolute;top:0;left:0;width:1200px;height:33px;background:var(--page);font-size:12px;font-weight:300;color:var(--muted)}
.topbar-item{position:absolute;top:10px;display:flex;align-items:center;gap:6px;white-space:nowrap}
.topbar-sep{position:absolute;top:0;width:1px;height:33px;background:var(--rule)}
.icon{width:13px;height:13px;flex:none;fill:none;stroke:var(--soft);stroke-width:1.2}

.header{position:absolute;top:33px;left:0;width:1200px;height:87px;background:var(--white)}
.brand{position:absolute;left:68px;top:21px;font-family:"Crimson Text",Georgia,serif;font-size:15px;line-height:17px;color:var(--ink);width:130px}
.nav{position:absolute;top:40px;left:641px;display:flex;font-family:"Crimson Text",Georgia,serif;font-size:14.5px;color:var(--ink);white-space:nowrap}
.nav a{margin-right:32px}
.nav a:last-child{margin-right:0}
.nav a.active{color:var(--accent)}

.hero{position:absolute;top:120px;left:0;width:1200px;height:507px;overflow:hidden;
  background:
    linear-gradient(90deg,rgba(0,0,0,0) 0%,rgba(0,0,0,0) 55%,rgba(107,58,36,.85) 72%,var(--wheel) 100%),
    linear-gradient(180deg,var(--sky) 0%,#bcd8ef 30%,var(--leaf) 52%,var(--thatch) 78%,#8a7a5c 100%)}
.hero-title{position:absolute;left:748px;top:22px;font-family:"Pinyon Script",cursive;font-size:60px;line-height:80px;color:#1a1a1a}
.hero-sub{position:absolute;left:641px;top:110px;font-family:"Crimson Text",Georgia,serif;font-size:24px;line-height:28px;color:#1e2a3a}

.section-title{position:absolute;font-family:"Crimson Text",Georgia,serif;font-size:21px;line-height:26px;color:#3a3a3a;text-align:center}
.about-text{position:absolute;left:89px;top:718px;width:276px;font-family:Arial,sans-serif;font-size:13px;line-height:16px;color:#333;text-indent:18px}
.more{position:absolute;font-family:Arial,sans-serif;font-size:13px;color:var(--link);font-weight:bold}

.downloads{position:absolute;left:504px;top:715px;list-style:none;font-family:Arial,sans-serif;font-size:13px;color:var(--link)}
.downloads li{height:28.5px;display:flex;align-items:flex-start;gap:6px}
.file{width:13px;height:15px;flex:none;fill:none;stroke:var(--link);stroke-width:1.2}

.contact{position:absolute;left:904px;top:716px;list-style:none;font-size:12px;font-weight:300;color:var(--muted)}
.contact li{height:24.8px;display:flex;align-items:flex-start;gap:6px;white-space:nowrap}

.customers{position:absolute;top:960px;left:60px;width:1080px;height:120px}
.customer{position:absolute;top:0;height:118px;display:flex;align-items:center;justify-content:center;gap:8px;font-family:"Crimson Text",Georgia,serif;font-size:19px;font-weight:600;color:#3a3a3a;white-space:nowrap}
.customer .dot{width:14px;height:14px;border-radius:50%;background:#b72a2a}

.footer-rule{position:absolute;top:1158px;left:74px;width:1054px;height:1px;background:var(--rule)}
.copyright{position:absolute;top:1170px;left:74px;font-family:Arial,sans-serif;font-size:12px;color:var(--soft)}
.footer-nav{position:absolute;top:1170px;right:72px;font-family:Arial,sans-serif;font-size:12px;color:var(--soft)}
</style>
</head>
<body>

<div class="topbar">
  <span class="topbar-item" style="left:62px"><svg class="icon" viewBox="0 0 13 13"><path d="M6.5 12S2.5 7.5 2.5 5a4 4 0 0 1 8 0c0 2.5-4 7-4 7z"/><circle cx="6.5" cy="5" r="1.4"/></svg>218 Harbour Row, Port Vila</span>
  <span class="topbar-sep" style="left:229px"></span>
  <span class="topbar-item" style="left:242px"><svg class="icon" viewBox="0 0 13 13"><rect x="3" y="1" width="7" height="11" rx="1"/><line x1="5.5" y1="10" x2="7.5" y2="10"/></svg>8 (041) 320 - 74 - 16</span>
  <span class="topbar-sep" style="left:370px"></span>
  <span class="topbar-item" style="left:383px"><svg class="icon" viewBox="0 0 13 13"><rect x="1" y="3" width="11" height="7.5"/><path d="M1 3l5.5 4 5.5-4"/></svg>desk@coralledger.example</span>
</div>

<header class="header">
  <a class="brand" href="#">Coral Ledger<br>Advisory Limited</a>
  <nav class="nav">
    <a class="active" href="#">Home</a>
    <a href="#">Who are we</a>
    <a href="#">Documents</a>
    <a href="#">Regulations &amp; Taxes</a>
    <a href="#">Contact</a>
  </nav>
</header>

<section class="hero" role="img" aria-label="Photo of thatched bungalows on stilts by a tropical shore with palm trees, and a close-up roulette wheel on the right">
  <h1 class="hero-title">Vanuatu</h1>
  <p class="hero-sub">A true paradise for online<br>gaming operators</p>
</section>

<h2 class="section-title" style="left:120px;top:669px;width:200px">About Us</h2>
<p class="about-text">Coral Ledger Advisory Limited is lorem ipsum dolor sit amet, consectetur adipisicing elit, sed do eiusmod tempor incididunt ut labore et dolore magna aliqua. Ut enim ad minim veniam, quis nostrud exercitation ullamco laboris nisi ut aliquip ex ea commodo consequat.</p>
<a class="more" href="#" style="left:298px;top:846px">Read more</a>

<h2 class="section-title" style="left:528px;top:669px;width:200px">Download</h2>
<ul class="downloads">
  <li><svg class="file" viewBox="0 0 13 15"><path d="M1 1h7l4 4v9H1z"/><path d="M8 1v4h4"/></svg><a href="#">Terms and conditions</a></li>
  <li><svg class="file" viewBox="0 0 13 15"><path d="M1 1h7l4 4v9H1z"/><path d="M8 1v4h4"/></svg><a href="#">Licenses for online operators</a></li>
  <li><svg class="file" viewBox="0 0 13 15"><path d="M1 1h7l4 4v9H1z"/><path d="M8 1v4h4"/></svg><a href="#">Taxes overwiew</a></li>
  <li><svg class="file" viewBox="0 0 13 15"><path d="M1 1h7l4 4v9H1z"/><path d="M8 1v4h4"/></svg><a href="#">Guide for starting in Vanuatu</a></li>
</ul>
<a class="more" href="#" style="left:668px;top:847px">Browse all files</a>

<h2 class="section-title" style="left:900px;top:669px;width:200px">Get in Touch</h2>
<ul class="contact">
  <li><svg class="icon" viewBox="0 0 13 13"><path d="M6.5 12S2.5 7.5 2.5 5a4 4 0 0 1 8 0c0 2.5-4 7-4 7z"/><circle cx="6.5" cy="5" r="1.4"/></svg>Adress: 218 Harbour Row, Port Vila</li>
  <li><svg class="icon" viewBox="0 0 13 13"><rect x="3" y="1" width="7" height="11" rx="1"/><line x1="5.5" y1="10" x2="7.5" y2="10"/></svg>Phone: 8 (041) 320 - 74 - 16</li>
  <li><svg class="icon" viewBox="0 0 13 13"><rect x="1" y="3" width="8" height="7"/><path d="M9 5.5l3-1.5v5l-3-1.5"/></svg>Skype: coralledger</li>
  <li><svg class="icon" viewBox="0 0 13 13"><rect x="1" y="3" width="11" height="7.5"/><path d="M1 3l5.5 4 5.5-4"/></svg>E-mail: desk@coralledger.example</li>
  <li><svg class="icon" viewBox="0 0 13 13"><circle cx="4" cy="9" r="2.5"/><path d="M5.8 7.2L11 2M9 4l1.5 1.5"/></svg>Weekend: from 9 am to 6 pm</li>
</ul>

<h2 class="section-title" style="left:528px;top:913px;width:200px">Our Customers</h2>
<div class="customers">
  <div class="customer" style="left:0;width:175px"><span class="dot"></span>Crown Hollow</div>
  <div class="customer" style="left:195px;width:165px"><span class="dot"></span>Reefline</div>
  <div class="customer" style="left:370px;width:140px">Palmstone Group</div>
  <div class="customer" style="left:525px;width:140px"><span class="dot"></span>Lantern Club</div>
  <div class="customer" style="left:690px;width:185px">Tidewater Casino</div>
  <div class="customer" style="left:925px;width:140px"><span class="dot"></span>Harbor 20</div>
</div>

<div class="footer-rule"></div>
<p class="copyright">Copyright © 2014 CLAL.</p>
<nav class="footer-nav"><a href="#">Home</a> | <a href="#">Who are we</a> | <a href="#">Documents</a> | <a href="#">Regulations &amp; Taxes</a> | <a href="#">Contact</a></nav>

</body>
</html>
```